I have a tallow based business and I want to streamline my products

I have roughly 10 items that I would like to make lebals for in order to streamline my business, I am attaching the current design and am willing to work with this but would also like to see if you come up with something different, my biggest seller is my facewash , my webpage is themeadowlyco,com my current designs are below- The newest one is the light brown version which I do like but I am not sure how that will integrate or be streamlined with the remaining products, If you believe it can look similar and still be attractive, I am ok with that too,

My current Label Project Needs:

Tallow + Magnesium Lotion biodegradable wheat bottle
Tallow Cream Face Wash - biodegradable what bottle
Tallow Body Butter 8 oz jar with bamboo lid
Tallow Deodorant will be printed on a Kraft Paper tube
Tallow Face Cream for Day wear 2 oz glass jar with bamboo lid
Vitamin C Serum 2 oz serum bottle with bamboo pump
Blue Algae Toner 4 oz glass bottle
Tallow + Hyaluronic 2oz face cream jar
'
My project is to display sustainable products, eco friendly packaging, organic , natural and holistic

I am ok with the newest label I attached but I am also ok with a minimalistic project, I would love to choose from a couple of designs.

Thank you so much

```html
<!DOCTYPE html>
<html lang="en">
<head>
<meta charset="utf-8">
<title>The Meadowly Co. – Label Set</title>
<link rel="stylesheet" href="https://fonts.googleapis.com/css2?family=Jost:wght@300;400;500;600&display=swap">
<style>
  :root{
    --ink:#3d4356;
    --page:#ffffff;
    --metal-dark:#b9bcc0;
    --metal-mid:#d5d7da;
    --metal-light:#eef0f2;
    --satin-a:#e6e6e8;
    --satin-b:#f7f7f8;
    --art-fill:#c4c7cd;
  }
  *{box-sizing:border-box;margin:0;padding:0}
  html,body{width:1200px;height:1200px;overflow:hidden;background:var(--page)}
  body{position:relative;font-family:"Jost",sans-serif;color:var(--ink)}

  .label{position:absolute;left:109px;width:990px;height:521px;overflow:hidden}
  .label--lotion{top:70px;
    background:linear-gradient(90deg,var(--metal-dark) 0%,var(--metal-mid) 22%,var(--metal-light) 34%,var(--metal-mid) 48%,var(--metal-light) 62%,#f4f5f6 70%,var(--metal-mid) 82%,var(--metal-dark) 100%)}
  .label--wash{top:616px;
    background:linear-gradient(160deg,var(--satin-b) 0%,var(--satin-a) 25%,var(--satin-b) 45%,var(--satin-a) 65%,var(--satin-b) 85%,var(--satin-a) 100%)}

  .brand-tab{position:absolute;left:379px;top:0;width:234px;height:58px;background:var(--ink);
    color:#fff;font-size:18px;font-weight:400;letter-spacing:.5px;display:flex;align-items:center;justify-content:center}

  .badge{position:absolute;width:90px;text-align:center;font-size:11px;font-weight:500;line-height:13.5px;letter-spacing:.3px}
  .badge__icon{display:block;width:44px;height:44px;margin:0 auto 12px;border:2px solid var(--ink);border-radius:10px}

  .maker{position:absolute;left:18px;top:420px;font-size:13.5px;line-height:22px;letter-spacing:.4px}
  .maker__name{font-size:17px;font-weight:600;letter-spacing:.6px}

  .element-tile{position:absolute;left:355px;top:106px;width:80px;height:80px;border:3px solid var(--ink);border-radius:6px;background:#e5e7ea}
  .element-tile__num{position:absolute;left:6px;top:5px;font-size:7px}
  .element-tile__mass{position:absolute;right:6px;top:5px;font-size:7px}
  .element-tile__sym{position:absolute;left:0;right:0;top:20px;text-align:center;font-size:28px;font-weight:600}
  .element-tile__name{position:absolute;left:0;right:0;bottom:7px;text-align:center;font-size:7px}

  .art{position:absolute;background:radial-gradient(ellipse at center,#9da2ad 0%,var(--art-fill) 55%,rgba(196,199,205,0) 72%)}
  .art--grazing{left:413px;top:108px;width:234px;height:184px}
  .art--head{left:532px;top:168px;width:172px;height:169px}

  .subtitle{position:absolute;left:324px;width:351px;text-align:center;font-size:28px;font-weight:500;top:312px;letter-spacing:.5px}
  .title-box{position:absolute;left:324px;top:352px;width:351px;height:55px;border:3px solid var(--ink);
    display:flex;align-items:center;justify-content:center;font-size:42px;font-weight:600;letter-spacing:1px}
  .tagline{position:absolute;font-size:13px;font-weight:500;line-height:17px;letter-spacing:.4px}
  .tagline--center{left:290px;width:420px;top:420px;text-align:center}
  .tagline--left{left:322px;top:421px}
  .net{position:absolute;left:324px;width:351px;text-align:center;font-size:16.5px;font-weight:600;top:490px;letter-spacing:.3px}

  .ingredients{position:absolute;left:782px;top:497px;width:467px;height:195px;transform-origin:0 0;transform:rotate(-90deg);
    font-size:15.5px;font-weight:300;line-height:21px}
  .ingredients__head{display:block;font-weight:600;letter-spacing:.5px;margin-bottom:1px}

  .grid{position:absolute;left:324px;top:111px;width:351px;height:289px}
  .grid__cell{position:absolute;border:3px solid var(--ink)}
  .grid__tallow{left:0;top:0;width:195px;height:56px;display:flex;align-items:center;padding-left:22px;font-size:28px;font-weight:500}
  .grid__cream{left:0;top:53px;width:195px;height:186px;display:flex;align-items:center;padding-left:22px;font-size:44px;font-weight:400}
  .grid__art{left:192px;top:0;width:159px;height:239px}
  .grid__title{left:0;top:236px;width:351px;height:53px;display:flex;align-items:center;justify-content:center;font-size:42px;font-weight:600;letter-spacing:.8px}
</style>
</head>
<body>

<section class="label label--lotion">
  <div class="brand-tab">THE MEADOWLY CO.</div>

  <div class="badge" style="left:35px;top:97px"><span class="badge__icon"></span>GRASS FED<br>TALLOW</div>
  <div class="badge" style="left:162px;top:97px"><span class="badge__icon"></span>ORGANIC<br>INGREDIENTS</div>
  <div class="badge" style="left:35px;top:203px"><span class="badge__icon"></span>HAND<br>CRAFTED</div>
  <div class="badge" style="left:162px;top:203px"><span class="badge__icon"></span>FAIR<br>TRADE</div>

  <div class="element-tile">
    <span class="element-tile__num">12</span><span class="element-tile__mass">24.305</span>
    <span class="element-tile__sym">Mg</span><span class="element-tile__name">Magnesium</span>
  </div>
  <div class="art art--grazing" role="img" aria-label="Engraved illustration of a grazing dairy cow"></div>

  <div class="subtitle">TALLOW + MAGNESIUM</div>
  <div class="title-box">BODY LOTION</div>
  <p class="tagline tagline--center">MAGNESIUM INFUSED LOTION THAT<br>PROMOTES SKIN NOURISHMENT AND HEALING</p>
  <div class="net">NET WT. 8OZ (236ML)</div>

  <div class="maker">MANUFACTURED BY<br><span class="maker__name">VERDANT HOLLOW ORGANICS</span><br>PO. BOX 4417 ASHBROOK, VA 23100<br>THEMEADOWLYCO.COM</div>

  <div class="ingredients"><span class="ingredients__head">OUR AMAZING INGREDIENTS:</span>Distilled Water, Lavender Hydrosol, Glycerin, Grass Fed Tallow, Daucus Carota (Carrot Seed Oil), Oenothera Biennis (Rosehip Oil), Simmondsia Chinensis(Jojoba Oil) Cocos Nucifera (Coconut Oil), Cucurbita Pepo Seed Oil (Pumpkin Seed Oil)Coenzyme Q10 ( CoQ10 )Niacinamide, Vitamin B3 Citrus Paradisi Seed Oil (Grapefruit Seed oil), Decyl Glucoside, Cetyl Alcohol Citric Acid, Xanthan Gum, Sodium Benzoate (Preservative)</div>
</section>

<section class="label label--wash">
  <div class="brand-tab">THE MEADOWLY CO.</div>

  <div class="badge" style="left:35px;top:97px"><span class="badge__icon"></span>GRASS FED<br>TALLOW</div>
  <div class="badge" style="left:162px;top:97px"><span class="badge__icon"></span>ORGANIC<br>INGREDIENTS</div>
  <div class="badge" style="left:35px;top:203px"><span class="badge__icon"></span>HAND<br>CRAFTED</div>
  <div class="badge" style="left:162px;top:203px"><span class="badge__icon"></span>FAIR<br>TRADE</div>

  <div class="grid">
    <div class="grid__cell grid__tallow">TALLOW</div>
    <div class="grid__cell grid__cream">CREAM</div>
    <div class="grid__cell grid__art"></div>
    <div class="grid__cell grid__title">FACE WASH</div>
  </div>
  <div class="art art--head" role="img" aria-label="Illustration of a dairy cow's head"></div>

  <p class="tagline tagline--left">CREAM LOTION THAT PROMOTES SKIN<br>NOURISHMENT AND HEALING</p>
  <div class="net">NET WT. 8OZ (236ML)</div>

  <div class="maker">MANUFACTURED BY<br><span class="maker__name">VERDANT HOLLOW ORGANICS</span><br>PO. BOX 4417 ASHBROOK, VA 23100<br>THEMEADOWLYCO.COM</div>

  <div class="ingredients"><span class="ingredients__head">OUR AMAZING INGREDIENTS:</span>Distilled Water, Lavender Hydrosol, Glycerin, Grass Fed Tallow, Daucus Carota (Carrot Seed Oil), Oenothera Biennis (Rosehip Oil), Simmondsia Chinensis(Jojoba Oil) Cocos Nucifera (Coconut Oil), Cucurbita Pepo Seed Oil (Pumpkin Seed Oil)Coenzyme Q10 ( CoQ10 )Niacinamide, Vitamin B3 Citrus Paradisi Seed Oil (Grapefruit Seed oil), Decyl Glucoside, Cetyl Alcohol Citric Acid, Xanthan Gum, Sodium Benzoate (Preservative)</div>
</section>

</body>
</html>
```